PREMIUM AGENCY High End Business Card - A+++ Designers Wanted

** DO NOT ATTEMPT TO CONTACT ME THROUGH SEARCHING ON ZINTREL OR EMAILING ME THROUGH MY WEBSITE **

I need a fresh, contemporary business card designed using the logo attached (BRONSALK)

I have attached the font for BRONSALK

It must have a premium look and feel. The business card size must be STANDARD size.

You can submit either/both VERTICAL or HORIZONTAL designs.

FRONT: It must have the following sample information on

Paul Ardley
Director Operations
Mobile +61 452 118 906
Email paulardley@bronsalk.com
www.bronsalk.com

The REAR of the business card must have the words

CREATE INSPIRE TOMORROW

as part of the design, in the same font (NEXA) attached.

The words do not need to be in capitals, or on the same line, please design this as you see it best working.

ADDITIONAL INFORMATION
======================

The BRONSALK logo must be on the front of the card

I want Ultraviolet printing on the final design, to enhance either the NAME of the person OR the BRONSALK logo OR the words on the back of the card.

Target Market(s)

Agency, Advertising Agency, Creative, Designers

Industry/Entity Type

Media

Contact Information for Business Card

Design Agency, Contemporary, Premium look and feel, High Quality

Font styles to use
Serif
Sans Serif
Other font styles liked:
• ATTACHED TO PROJECT

Requirements
Must have
• BLACK & WHITE as the primary design, and if you feel there can be a highlighted colour, then this can be used.
• The Logo ICON attached is blue, this colour must not be changed.
• I have attached the partner brand BRONSALK MEDIA incase you need to manipulate the original files.
• ** DO NOT ATTEMPT TO CONTACT ME THROUGH SEARCHING ON ZINTREL OR EMAILING ME THROUGH MY WEBSITE **
Nice to have
• Must be Premium. I have attached some sample designs, that I like that would be a good inspiration for where this can be taken.
• My favourite design is is the KESTRAVUE2-BUSINESSCARD-TEMPLATE
Should not have
• No funny or silly standard / off the shelf designs

```html
<!DOCTYPE html>
<html lang="en">
<head>
<meta charset="utf-8">
<title>Bronsalk Media – Business Card</title>
<link rel="stylesheet" href="https://fonts.googleapis.com/css2?family=Montserrat:wght@300;400;600;700&display=swap">
<style>
  :root {
    --bg: #ececec;
    --ink: #0b0b0b;
    --charcoal: #232323;
    --white: #ffffff;
    --blue: #29a8e0;
    --grey-text: #3a3a3a;
    --muted: #555;
  }
  * { box-sizing: border-box; margin: 0; padding: 0; }
  html, body { width: 1200px; height: 1200px; overflow: hidden; }
  body {
    background: var(--bg);
    font-family: "Montserrat", sans-serif;
    position: relative;
  }
  .brand-header {
    position: absolute; top: 42px; right: 40px;
    display: flex; align-items: center; gap: 18px;
  }
  .brand-dot { width: 34px; height: 34px; border-radius: 50%; background: var(--blue); }
  .brand-name {
    font-weight: 600; font-size: 52px; letter-spacing: 5px; color: #222;
  }
  .card {
    position: absolute; left: 320px; width: 560px; height: 320px;
    box-shadow: 0 14px 30px rgba(0,0,0,.18);
    overflow: hidden;
  }
  .card-back { top: 210px; background: var(--ink); display: flex; align-items: center; justify-content: center; }
  .back-name {
    font-weight: 700; font-size: 40px; letter-spacing: 6px; color: var(--blue);
  }
  .card-front { top: 620px; background: var(--white); }
  .front-band { position: absolute; inset: 0; }
  .front-logo {
    position: absolute; left: 34px; top: 44px;
    display: flex; align-items: center; gap: 14px;
  }
  .front-logo .brand-dot { width: 22px; height: 22px; }
  .front-logo-name {
    font-weight: 600; font-size: 30px; letter-spacing: 4px; color: var(--white);
  }
  .person { position: absolute; left: 40px; bottom: 48px; }
  .person-name {
    font-weight: 700; font-size: 30px; letter-spacing: 1px; color: var(--grey-text);
    text-transform: uppercase;
  }
  .person-role {
    font-weight: 400; font-size: 11px; letter-spacing: 1px; color: var(--blue);
    text-transform: uppercase; margin-top: 2px;
  }
  .divider {
    position: absolute; left: 300px; top: 205px; width: 1px; height: 80px; background: #444;
  }
  .contact { position: absolute; left: 322px; top: 200px; list-style: none; }
  .contact li {
    display: flex; align-items: center; gap: 10px;
    font-size: 12px; color: var(--muted); height: 28px;
  }
  .contact svg { width: 14px; height: 14px; flex: none; }
</style>
</head>
<body>
  <header class="brand-header">
    <span class="brand-dot"></span>
    <span class="brand-name">BRONSALK MEDIA</span>
  </header>

  <section class="card card-back" aria-label="Card back">
    <span class="back-name">BRONSALK</span>
  </section>

  <section class="card card-front" aria-label="Card front">
    <svg class="front-band" viewBox="0 0 560 320" preserveAspectRatio="none">
      <path d="M0 0 H560 V40 H470 V110 H230 V190 H0 Z" fill="var(--ink)"/>
      <rect x="400" y="40" width="70" height="24" fill="var(--blue)"/>
      <rect x="330" y="64" width="70" height="46" fill="var(--charcoal)"/>
      <rect x="150" y="110" width="80" height="26" fill="var(--blue)"/>
      <rect x="80" y="136" width="70" height="54" fill="var(--charcoal)"/>
    </svg>
    <div class="front-logo">
      <span class="brand-dot"></span>
      <span class="front-logo-name">BRONSALK</span>
    </div>
    <div class="person">
      <p class="person-name">Paul Ardley</p>
      <p class="person-role">Director Operations</p>
    </div>
    <span class="divider"></span>
    <ul class="contact">
      <li>
        <svg viewBox="0 0 14 14"><rect x="3.5" y="1" width="7" height="12" rx="1.5" fill="none" stroke="var(--blue)" stroke-width="1.5"/></svg>
        +61 452 118 906
      </li>
      <li>
        <svg viewBox="0 0 14 14"><rect x="1" y="3" width="12" height="8" fill="var(--blue)"/><path d="M1 3 L7 8 L13 3" fill="none" stroke="#fff" stroke-width="1"/></svg>
        paulardley@bronsalk.com
      </li>
      <li>
        <svg viewBox="0 0 14 14"><circle cx="7" cy="7" r="5.5" fill="none" stroke="var(--blue)" stroke-width="1.3"/><path d="M1.5 7 H12.5 M7 1.5 V12.5" stroke="var(--blue)" stroke-width="1"/></svg>
        www.bronsalk.com
      </li>
    </ul>
  </section>
</body>
</html>
```